Cosmetic Label Design for a Sunless Tanner

We need a label for a new sunless tanner. The label dye will be 2.5 inches in height by 6 inches in width. It will be laser printed by Brintova.net The label will be printed on gloss laminated white polypropylene self-adhesive material. A full project description can be found in the attached Word file. The label copy is also included in a Word file.

Target Market(s)

Females aged 18 to 35

Font styles to use
Serif

Colors

Designer to choose colors to be used in the design.

Requirements
Must have
• Clean look. Strong brand image.
Nice to have
• This is the first product in a future line. The design should have the ability to move to other products.
Should not have
• Too heavy. More than 4 colors. Fonts that are whimsical. Cursive writing. No cartoon like illustrations.

```html
<!DOCTYPE html>
<html lang="en">
<head>
<meta charset="utf-8">
<title>Solvaine Sunless Tanner Label</title>
<link rel="stylesheet" href="https://fonts.googleapis.com/css2?family=Cormorant+Garamond:wght@300;500&display=swap">
<style>
  :root {
    --page-grey: #d3d6da;
    --label-black: #0d0d0e;
    --teal: #5fb3a1;
    --teal-deep: #4f9e8e;
    --ink-white: #f4f6f5;
    --volume-teal: #6cc0ad;
  }
  html, body {
    margin: 0;
    padding: 0;
    width: 1200px;
    height: 1200px;
    overflow: hidden;
    background: var(--page-grey);
  }
  .label {
    position: absolute;
    left: 0;
    top: 350px;
    width: 1200px;
    height: 500px;
    background: var(--label-black);
    overflow: hidden;
  }
  .label-art {
    position: absolute;
    inset: 0;
  }
  .emblem-text {
    position: absolute;
    left: 0;
    width: 1200px;
    margin: 0;
    text-align: center;
    color: var(--ink-white);
    font-family: "Cormorant Garamond", Georgia, serif;
  }
  .eyebrow {
    top: 78px;
    font-weight: 300;
    font-size: 32px;
    line-height: 1;
    letter-spacing: 0.16em;
    padding-left: 0.16em;
  }
  .brand-name {
    top: 112px;
    font-weight: 300;
    font-size: 112px;
    line-height: 1;
    letter-spacing: 0.01em;
  }
  .brand-rule {
    position: absolute;
    left: 450px;
    top: 248px;
    width: 300px;
    height: 3px;
    background: var(--ink-white);
  }
  .tagline {
    top: 266px;
    font-weight: 500;
    font-size: 22px;
    line-height: 34px;
    letter-spacing: 0.26em;
    padding-left: 0.26em;
  }
  .volume {
    top: 452px;
    font-weight: 500;
    font-size: 21px;
    line-height: 1;
    letter-spacing: 0.06em;
    color: var(--volume-teal);
  }
</style>
</head>
<body>
  <main class="label">
    <svg class="label-art" width="1200" height="500" viewBox="0 0 1200 500" xmlns="http://www.w3.org/2000/svg">
      <defs>
        <linearGradient id="emblemFill" x1="0" y1="0" x2="0" y2="1">
          <stop offset="0" stop-color="#63b8a6"/>
          <stop offset="1" stop-color="#4f9e8e"/>
        </linearGradient>
        <radialGradient id="foliageGlow" cx="0.5" cy="0.5" r="0.5">
          <stop offset="0" stop-color="#f4f6f5" stop-opacity="0.55"/>
          <stop offset="0.7" stop-color="#f4f6f5" stop-opacity="0.22"/>
          <stop offset="1" stop-color="#f4f6f5" stop-opacity="0"/>
        </radialGradient>
      </defs>
      <g class="foliage-left" role="img" aria-label="White line-drawn leaves and flowers framing the left side of the emblem">
        <ellipse cx="388" cy="235" rx="62" ry="200" fill="url(#foliageGlow)"/>
      </g>
      <g class="foliage-right" role="img" aria-label="White line-drawn leaves and flowers framing the right side of the emblem">
        <ellipse cx="812" cy="235" rx="62" ry="200" fill="url(#foliageGlow)"/>
      </g>
      <circle class="emblem-disc" cx="600" cy="235" r="205" fill="url(#emblemFill)"/>
    </svg>

    <p class="emblem-text eyebrow">Certified</p>
    <h1 class="emblem-text brand-name">Solvaine</h1>
    <div class="brand-rule"></div>
    <p class="emblem-text tagline">SKIN NOURISHING<br>SUNLESS TANNER</p>
    <p class="emblem-text volume">8 FL OZ (237ML)</p>
  </main>
</body>
</html>
```